Bref créative
Harbor Crest card design
biz card
Bright & Fun-filled
Dennis Pollard
Senior Healthcare Specialist
P.O. Box 42916
Asheville, NC 28492
dpollard4@velmora.net
please include my picture on the business card. I will attach it in the upload section.
please add the info that I currently have on the back of my business card now. I will upload that as well.
Front of Current Business Card
Back of Current Business Card
Headshot for Card
new logo to use for card front

```html
<!DOCTYPE html>
<html lang="en">
<head>
<meta charset="utf-8">
<title>Harbor Crest Inc business cards</title>
<link rel="stylesheet" href="https://fonts.googleapis.com/css2?family=Source+Sans+3:wght@400;600;700&display=swap">
<style>
  :root {
    --page: #eceae6;
    --card: #ffffff;
    --navy: #1d4f86;
    --orange: #f07a1e;
    --ink-light: #ffffff;
    --photo-top: #8fa3b8;
    --photo-bottom: #3f5468;
    --shadow: rgba(0, 0, 0, 0.18);
  }
  * { box-sizing: border-box; margin: 0; padding: 0; }
  html, body {
    width: 1200px; height: 852px; overflow: hidden;
    background: var(--page);
    font-family: "Source Sans 3", Arial, sans-serif;
  }
  .sheet { position: relative; width: 1200px; height: 852px; }
  .card {
    position: absolute; top: 266px;
    width: 540px; height: 320px;
    border-radius: 18px; overflow: hidden;
    background: var(--card);
    box-shadow: 0 6px 18px var(--shadow);
  }
  .card--front { left: 40px; }
  .card--back { left: 620px; }
  .card__backdrop { position: absolute; inset: 0; }
  .headshot {
    position: absolute; width: 86px; height: 100px;
    border: 3px solid var(--card);
    background: linear-gradient(180deg, var(--photo-top), var(--photo-bottom));
  }
  .card--front .headshot { left: 30px; top: 36px; }
  .card--back .headshot { right: 36px; top: 26px; }
  .contact { position: absolute; color: var(--ink-light); }
  .card--front .contact { left: 30px; top: 150px; }
  .card--back .contact { right: 36px; top: 138px; text-align: right; }
  .contact__name { font-size: 16px; font-weight: 700; line-height: 1.1; }
  .contact__title { font-size: 11px; font-weight: 600; margin-top: 2px; }
  .contact__address { font-size: 13px; line-height: 1.25; margin-top: 10px; }
  .contact__lines { list-style: none; margin-top: 14px; font-size: 13px; line-height: 1.45; }
  .contact__lines li { display: flex; align-items: center; gap: 7px; }
  .card--back .contact__lines li { justify-content: flex-end; }
  .contact__lines svg { width: 13px; height: 13px; flex: none; }
  .brand {
    position: absolute; display: flex; align-items: center; gap: 9px;
    color: var(--navy); font-size: 26px; font-weight: 700; letter-spacing: 0.3px;
    white-space: nowrap; line-height: 1;
  }
  .brand__dot {
    width: 16px; height: 16px; border-radius: 50%; background: var(--navy);
  }
  .card--front .brand { left: 262px; top: 146px; }
  .card--back .brand { left: 54px; top: 146px; }
</style>
</head>
<body>
<main class="sheet">

  <section class="card card--front">
    <svg class="card__backdrop" viewBox="0 0 540 320" width="540" height="320" aria-hidden="true">
      <path d="M0 0 H244 Q176 160 244 320 H0 Z" fill="var(--orange)"/>
      <path d="M0 0 H236 Q168 160 236 320 H0 Z" fill="var(--navy)"/>
    </svg>
    <div class="headshot" role="img" aria-label="Headshot of Dennis Pollard"></div>
    <div class="contact">
      <p class="contact__name">Dennis Pollard</p>
      <p class="contact__title">Senior Healthcare Specialist</p>
      <p class="contact__address">P.O. Box 42916<br>Asheville, NC 28492</p>
      <ul class="contact__lines">
        <li><svg viewBox="0 0 16 16"><path d="M4 1 L6 5 L4.5 6.5 Q6 10 9.5 11.5 L11 10 L15 12 L13.5 15 Q3 14 1 2.5 Z" fill="currentColor"/></svg>828-555-0143</li>
        <li><svg viewBox="0 0 16 16"><rect x="4" y="1" width="8" height="14" rx="1.5" fill="currentColor"/><rect x="5.5" y="3" width="5" height="8" fill="var(--navy)"/></svg>828-555-0188</li>
        <li><svg viewBox="0 0 16 16"><rect x="1" y="3" width="14" height="10" rx="1" fill="currentColor"/><path d="M1.5 3.5 L8 9 L14.5 3.5" fill="none" stroke="var(--navy)" stroke-width="1.4"/></svg>dpollard4@velmora.net</li>
      </ul>
    </div>
    <div class="brand"><span class="brand__dot"></span>Harbor Crest Inc</div>
  </section>

  <section class="card card--back">
    <svg class="card__backdrop" viewBox="0 0 540 320" width="540" height="320" aria-hidden="true">
      <path d="M540 0 H300 Q368 160 300 320 H540 Z" fill="var(--orange)"/>
      <path d="M540 0 H308 Q376 160 308 320 H540 Z" fill="var(--navy)"/>
    </svg>
    <div class="brand"><span class="brand__dot"></span>Harbor Crest Inc</div>
    <div class="headshot" role="img" aria-label="Headshot of Dennis Pollard"></div>
    <div class="contact">
      <p class="contact__name">Dennis Pollard</p>
      <p class="contact__title">Senior Healthcare Specialist</p>
      <p class="contact__address">P.O. Box 42916<br>Asheville, NC 28492</p>
      <ul class="contact__lines">
        <li>828-555-0143<svg viewBox="0 0 16 16"><path d="M4 1 L6 5 L4.5 6.5 Q6 10 9.5 11.5 L11 10 L15 12 L13.5 15 Q3 14 1 2.5 Z" fill="currentColor"/></svg></li>
        <li>828-555-0188<svg viewBox="0 0 16 16"><rect x="4" y="1" width="8" height="14" rx="1.5" fill="currentColor"/><rect x="5.5" y="3" width="5" height="8" fill="var(--navy)"/></svg></li>
        <li>dpollard4@velmora.net<svg viewBox="0 0 16 16"><rect x="1" y="3" width="14" height="10" rx="1" fill="currentColor"/><path d="M1.5 3.5 L8 9 L14.5 3.5" fill="none" stroke="var(--navy)" stroke-width="1.4"/></svg></li>
      </ul>
    </div>
  </section>

</main>
</body>
</html>
```